Tildens Biscuit Barn Website

I need a website for a diner/restaurant that has been established in a farming, oil and industrial community for over 15 years. The website needs to be simple in design, but that should demonstrate the mastery of skills of the designer. Our diner/restaurant is family oriented, patriotic but very rustic
Fb Address is fb.me/TildensBarn

Pictures of the restaurant

https://www.filecrate-example.net/s/qk72hdw01/Tildens_05.jpg

Pictures of About us

https://www.filecrate-example.net/sh/zm40vrt88/AboutUsPhotos

Article about Tilden's
https://www.filecrate-example.net/s/wp31nbx57/TildensBiscuitBarn1.PDF
https://www.filecrate-example.net/s/hy65lcu29/TildensBiscuitBarn2.PDF

Reason: I was slow to update with information.

Reason: I am just getting feedback to the designs posted. I wasn't sure of the limited feedback was limiting designers from submitting designs. That and running a business with 25 employees open 12 hours a day, being here 2 hours prior and 2-3 hours after makes for long days.

I've increased the first place prize and also added funds to the second and third place prizes for your effort.

I just need the files in PSD, not HTML 5 as originally requested. We can handle getting the coding part.

Ill have the contest finalized by Monday. Thanks for your patience.

Target Market(s)

Cross section of adults from 18-35 & 35-55.

Industry/Entity Type

Industrial

Font styles to use
Other font styles liked:
• ff tisa web pro or garamond premier pro

Requirements
Must have
• Must be clean, look nice and not look like an afterthought.
Nice to have
• Please see the last two documents for information about our restaurant, which was featured in our local newspaper.

```html
<!DOCTYPE html>
<html lang="en">
<head>
<meta charset="utf-8">
<title>Tilden's Biscuit Barn</title>
<link href="https://fonts.googleapis.com/css2?family=Open+Sans:wght@400;600;700&family=Oswald:wght@400;600&family=Roboto+Slab:wght@400;700&family=Dancing+Script:wght@700&display=swap" rel="stylesheet">
<style>
:root{
  --red:#b3121c;--red-dark:#8a0c14;--ink:#2a2a2a;--grey:#6b6b6b;--line:#dcdcdc;
  --page:#f0efed;--white:#fff;--footer:#333335;--footer-deep:#232324;--panel:#3d3d3f;
  --amber:#e0a21a;
}
*{box-sizing:border-box;margin:0;padding:0}
html,body{width:1200px;height:2968px;overflow:hidden}
body{position:relative;background:var(--page);font-family:"Open Sans",Arial,sans-serif;color:var(--ink);font-size:13px}
.abs{position:absolute}
.ph{position:absolute;display:block}
.title-sans{font-family:"Oswald",Arial,sans-serif;text-transform:uppercase;letter-spacing:.5px}
.script{font-family:"Dancing Script",cursive}
.slab{font-family:"Roboto Slab",Georgia,serif}

/* header */
.site-header{left:0;top:0;width:1200px;height:100px;background:var(--white)}
.brand{left:70px;top:18px;display:flex;align-items:center;gap:12px}
.brand-mark{width:22px;height:22px;background:var(--red)}
.brand-name{font-family:"Roboto Slab",Georgia,serif;font-weight:700;font-size:30px;color:var(--red)}
.main-nav{left:320px;top:58px;display:flex;border-bottom:3px solid var(--red)}
.main-nav a{display:block;width:111px;height:38px;line-height:38px;text-align:center;font-family:"Oswald",sans-serif;font-size:15px;color:var(--ink);text-decoration:none;background:#f7f7f7;border-right:1px solid #e4e4e4}
.main-nav a.active{background:var(--red);color:#fff}

/* hero */
.hero{left:0;top:100px;width:1200px;height:428px;background:linear-gradient(120deg,#6b2a16 0%,#a4461f 35%,#c9562a 55%,#7a3a1c 80%,#3e2a20 100%)}
.hero-strip{left:0;top:528px;width:1200px;height:10px;background:var(--red-dark)}
.daily{left:72px;top:145px;width:253px;height:333px;background:var(--red);box-shadow:0 3px 10px rgba(0,0,0,.4)}
.daily-tag{left:0;top:0;width:253px;height:36px;background:var(--amber);color:#fff;font-family:"Oswald",sans-serif;font-size:15px;line-height:36px;padding-left:14px}
.daily-art{left:10px;top:46px;width:233px;height:277px;background:radial-gradient(circle at 65% 35%,#fff 0 30%,#e9d6c4 45%,#c2111a 70%)}
.daily-text{left:20px;top:55px;color:var(--ink);font-size:24px;line-height:26px}
.fresh{left:806px;top:287px;width:308px;height:54px;background:var(--red);color:#fff;font-family:"Oswald",sans-serif;font-size:20px;line-height:54px;text-align:center}
.open{left:880px;top:343px;width:234px;height:28px;background:#fff;font-size:11px;line-height:28px;text-align:center;color:var(--ink)}
.hero-arrows{left:1044px;top:370px;display:flex;gap:4px}
.hero-arrows span{width:34px;height:40px;background:#fff;display:flex;align-items:center;justify-content:center}
.hero-bar{left:342px;top:420px;width:774px;height:68px;background:var(--red);color:#fff;padding:12px 16px}
.hero-bar .l1{font-family:"Oswald",sans-serif;font-size:17px}
.hero-bar .l2{font-family:"Oswald",sans-serif;font-size:15px;color:#f4d8d8}
.hero-bar .dl{position:absolute;right:20px;top:18px;font-family:"Oswald",sans-serif;font-style:normal;font-size:18px;color:#ffd7a0}

/* menu + featured */
.menu-box{left:81px;top:574px;width:238px;height:356px;background:#fff}
.menu-head{height:44px;background:var(--red);color:#fff;font-family:"Oswald",sans-serif;font-size:17px;line-height:44px;padding-left:12px}
.menu-item{position:relative;height:72px;margin-top:8px}
.menu-item .thumb{left:10px;top:0;width:150px;height:66px}
.menu-item .price{position:absolute;right:10px;top:16px;width:70px;height:36px;background:var(--red);color:#fff;font-weight:700;font-size:16px;line-height:36px;text-align:center}
.menu-row{display:flex;justify-content:space-between;align-items:center;height:41px;border-top:1px solid var(--line);padding:0 12px;font-size:14px;color:var(--grey)}
.menu-row i{width:18px;height:18px;border-radius:50%;background:#9a9a9a;color:#fff;font-style:normal;font-size:14px;line-height:18px;text-align:center}
.menu-list{margin-top:26px}
.featured{left:348px;top:574px;width:772px;height:356px;background:#fff}
.sec-head{height:44px;border-bottom:1px solid var(--line);font-family:"Oswald",sans-serif;font-size:17px;line-height:44px;padding-left:18px;color:var(--ink);background:#f6f6f6}
.dish{top:93px;width:222px;height:218px}
.dish-price{width:72px;height:72px;border-radius:50%;background:var(--red);border:4px solid #fff;color:#fff;font-weight:700;font-size:17px;line-height:64px;text-align:center}
.nav-dot{width:22px;height:22px;border-radius:50%;background:#555;color:#fff;font-size:13px;text-align:center;line-height:22px}

/* blog */
.blog-title{left:81px;top:970px;font-family:"Roboto Slab",serif;font-weight:700;font-size:28px}
.blog-rule{left:81px;top:1020px;width:687px;height:2px;background:var(--line)}
.date-box{background:var(--red);color:#fff;text-align:center;font-weight:700}
.post-date{left:81px;top:1044px;width:62px;height:66px}
.post-date b{display:block;font-size:26px;line-height:34px}
.post-date small{font-size:11px}
.post-meta{left:156px;top:1044px;font-size:11px;color:var(--grey)}
.post-heading{left:156px;top:1064px;font-family:"Roboto Slab",serif;font-size:21px;font-weight:700}
.post-img{left:81px;top:1125px;width:221px;height:215px}
.post-body{left:314px;top:1125px;width:214px;font-size:11px;line-height:16px;color:var(--grey)}
.post-body h4{font-family:"Oswald",sans-serif;font-weight:400;font-size:15px;color:var(--ink);margin-bottom:6px}
.post-body p{margin-bottom:8px}
.mini-posts{left:545px;top:1125px;width:223px}
.mini{display:flex;gap:6px;height:76px;border-bottom:1px solid var(--line);padding-top:6px}
.mini .d{width:30px;height:60px;font-size:15px;line-height:20px;padding-top:8px}
.mini .d small{display:block;font-size:9px}
.mini .t{width:64px;height:60px}
.mini .x{font-size:12px;font-weight:700;line-height:16px;padding-top:6px}
.mini .x span{display:block;font-weight:400;font-size:10px;color:var(--grey)}

.critic{left:792px;top:976px;width:328px;height:336px;background:#fff}
.critic-head{height:74px;background:var(--red);color:#fff;text-align:center;padding-top:10px}
.critic-head h3{font-family:"Roboto Slab",serif;font-size:26px;font-weight:700}
.critic-head p{font-size:13px;color:#f7cfcf}
.avatar{left:136px;top:80px;width:56px;height:56px;border-radius:50%;background:#8a5a44;border:3px solid #fff}
.quote{left:14px;top:145px;width:300px;height:74px;background:#f4f4f4;border:1px solid var(--line);font-size:11px;line-height:16px;color:var(--grey);padding:12px 14px 0 34px}
.quote::before{content:"\201C";position:absolute;left:10px;top:2px;font-size:30px;color:var(--amber);font-family:Georgia,serif}
.review-field{left:14px;top:225px;width:300px;height:68px;background:#e6e6e6}
.review-btn{left:14px;top:304px;width:300px;height:28px;background:var(--red);color:#fff;font-size:11px;font-weight:700;text-align:center;line-height:28px}

/* happy hour banner */
.deal{left:81px;top:1450px;width:1039px;height:116px;background:linear-gradient(90deg,#2e2e30 0%,#3b3b3d 60%,#2e2e30 100%);overflow:hidden}
.deal-red{left:0;top:0;width:270px;height:116px;background:var(--red)}
.deal-plate{left:240px;top:8px;width:100px;height:100px;border-radius:50%;background:radial-gradient(circle,#d26a2a 0 40%,#fff 42% 100%)}
.deal-script{left:22px;top:26px;color:#fff;font-size:28px;line-height:32px}
.deal-copy{left:380px;top:24px;color:#fff;font-family:"Open Sans",sans-serif;font-weight:700;font-size:30px;line-height:36px;text-align:center;width:500px}
.deal-badge{left:900px;top:28px;width:130px;height:60px;background:var(--red);color:#fff;font-size:26px;text-align:center;line-height:60px}

/* calendar row */
.today{left:81px;top:1618px;width:203px;height:296px;background:var(--red);color:#fff;text-align:center}
.today .day{font-family:"Oswald",sans-serif;font-size:16px;margin-top:26px}
.today .num{font-family:"Oswald",sans-serif;font-size:120px;line-height:130px}
.today .time{font-size:12px;border-top:1px solid rgba(255,255,255,.5);margin:10px 20px 0;padding-top:10px}
.today .evt{font-family:"Oswald",sans-serif;font-size:22px}
.cal{left:284px;top:1618px;width:232px;height:296px;background:#fff;padding:10px}
.cal-head{display:flex;justify-content:space-between;font-weight:700;font-size:14px;border-bottom:1px solid var(--line);padding-bottom:6px}
.cal-grid{display:grid;grid-template-columns:repeat(7,1fr);row-gap:10px;margin-top:10px;font-size:12px;text-align:center;color:var(--grey)}
.cal-grid b{color:var(--ink)}
.cal-grid .on{color:#fff;background:var(--red);border-radius:50%}
.events{left:527px;top:1618px;width:329px;height:296px;background:var(--panel)}
.events-head{height:36px;background:#b0b0b0;color:#fff;font-family:"Oswald",sans-serif;font-size:17px;line-height:36px;padding-left:14px}
.evt-row{position:relative;height:130px}
.evt-row .pic{left:0;top:0;width:163px;height:130px}
.evt-row .info{position:absolute;left:175px;top:12px;width:145px;color:#fff}
.evt-row .info b{font-family:"Oswald",sans-serif;font-size:40px;line-height:44px;font-weight:400}
.evt-row .info em{font-style:normal;font-size:13px;font-weight:700;display:block}
.evt-row .info p{font-size:10px;line-height:14px;color:#ccc}
.meet{left:879px;top:1618px;width:241px;height:296px;background:#fff}
.meet-head{height:60px;background:var(--red);color:#fff;font-family:"Roboto Slab",serif;font-weight:700;font-size:26px;line-height:60px;padding-left:12px;display:flex;justify-content:space-between;padding-right:12px;align-items:center}
.map{left:0;top:60px;width:241px;height:204px;background:#e8e4dc}
.meet-foot{left:0;top:264px;width:241px;height:32px;background:var(--red);color:#fff;font-size:11px;font-weight:700;text-align:right;padding-right:12px;line-height:32px}

/* chef row */
.chef-photo{left:81px;top:1972px;width:258px;height:284px;background:linear-gradient(180deg,#e9e6e2,#b9b3ad)}
.chef-social{left:81px;top:2220px;width:258px;height:36px;background:rgba(0,0,0,.7);display:flex;gap:16px;align-items:center;padding-left:14px}
.chef-social span,.foot-social span{width:16px;height:16px;background:#ddd}
.chef-info{left:339px;top:1972px;width:517px;height:284px;background:#fff}
.chef-head{height:56px;background:var(--red);color:#fff;font-family:"Roboto Slab",serif;font-weight:700;font-size:24px;line-height:56px;padding-left:16px}
.chef-arrows{position:absolute;right:0;top:0;display:flex}
.chef-arrows span{width:44px;height:56px;background:#444;border-left:1px solid #222;display:flex;align-items:center;justify-content:center}
.chef-sub{left:16px;top:70px;font-weight:700;font-size:13px}
.chef-list{left:16px;top:96px;width:490px;display:grid;grid-template-columns:1fr 1fr;gap:4px 20px;font-size:11px;color:var(--grey);list-style:none}
.chef-list li::before{content:"\25A0";color:var(--red);font-size:8px;margin-right:6px;vertical-align:middle}
.skills{left:16px;top:170px;display:flex;gap:38px}
.skill{text-align:center;font-size:10px;font-weight:700;width:90px}
.video{left:879px;top:1972px;width:241px;height:284px;background:#fff}
.video-head{height:56px;background:var(--panel);color:#fff;padding:10px 12px}
.video-head b{font-size:14px;display:block}
.video-head small{font-size:10px;color:#ccc}
.video-img{left:0;top:56px;width:241px;height:198px}
.video-bar{left:0;top:254px;width:241px;height:30px;background:#222}

/* footer */
.footer{left:0;top:2334px;width:1200px;height:363px;background:var(--footer)}
.f-title{font-weight:700;font-size:15px;color:#fff}
.f-col{top:2372px}
.f-item{display:flex;gap:10px;height:80px;align-items:flex-start;border-bottom:1px solid #444;padding-top:10px;color:#ccc;font-size:11px;line-height:15px}
.f-item .th{width:82px;height:58px;flex:none}
.f-item .dd{width:30px;height:58px;font-size:13px;line-height:18px;padding-top:8px;flex:none}
.f-item .dd small{display:block;font-size:9px}
.input{height:32px;background:#fff;margin-top:12px;font-size:11px;color:#999;padding:8px 10px}
.textarea{height:82px}
.submit{width:78px;height:28px;background:var(--red);color:#fff;font-size:11px;font-weight:700;text-align:center;line-height:28px;margin-top:12px}
.clock{left:880px;top:2344px;width:240px;height:200px}
.reserve{left:880px;top:2552px;width:240px;height:44px;background:#fff;font-size:11px;font-weight:700;padding:6px 10px;line-height:16px}
.reserve b{color:var(--red)}
.tweet{left:0;top:2697px;width:1200px;height:36px;background:#e9e9e9;display:flex;align-items:center;padding-left:81px;gap:14px;font-size:11px;color:var(--grey)}
.tweet .ic{width:22px;height:22px;border-radius:50%;background:#555}
.dots{position:absolute;right:81px;top:12px;display:flex;gap:10px}
.dots i{width:12px;height:12px;border-radius:50%;background:#999}
.dots i.on{background:#555}
.collection{left:0;top:2733px;width:1200px;height:190px;background:var(--footer)}
.coll-title{left:81px;top:2756px}
.coll-item{top:2790px;display:flex;gap:12px;width:320px}
.coll-item .th{width:140px;height:70px;flex:none}
.coll-item b{display:block;color:#fff;font-size:12px;line-height:16px}
.coll-item span{color:#aaa;font-size:10px;line-height:14px}
.base{left:0;top:2923px;width:1200px;height:45px;background:var(--footer-deep);color:#aaa;font-size:11px;line-height:45px;padding-left:81px}
.to-top{left:574px;top:2908px;width:52px;height:34px;border-radius:26px 26px 0 0;background:var(--red);display:flex;align-items:center;justify-content:center}
.foot-social{right:81px;top:2936px;display:flex;gap:6px}
.foot-social span{width:22px;height:22px;background:#555}
</style>
</head>
<body>

<header class="site-header abs">
  <div class="brand abs"><span class="brand-mark"></span><span class="brand-name">Tilden's Biscuit Barn</span></div>
  <nav class="main-nav abs">
    <a class="active" href="#">HOME</a><a href="#">MENU</a><a href="#">BLOG</a><a href="#">EVENTS</a><a href="#">SHOP</a><a href="#">PAGES</a><a href="#">CONTACT US</a>
  </nav>
</header>

<section class="hero abs" role="img" aria-label="Close-up photo of a rustic bowl of stewed beans, peppers and fresh herbs"></section>
<div class="hero-strip abs"></div>
<aside class="daily abs">
  <div class="daily-tag abs">COFFEE OF THE DAY</div>
  <div class="daily-art ph" role="img" aria-label="Illustration of a chef presenting a plate of pasta"></div>
  <div class="daily-text abs script">Deliciousness<br>made for you</div>
</aside>
<div class="fresh abs">FRESH MEALS EVERYDAY</div>
<div class="open abs">OPEN ALL WEEK: 10AM – 11PM</div>
<div class="hero-arrows abs">
  <span><svg width="10" height="14"><path d="M8 1 2 7l6 6" stroke="#333" stroke-width="2" fill="none"/></svg></span>
  <span><svg width="10" height="14"><path d="M2 1l6 6-6 6" stroke="#333" stroke-width="2" fill="none"/></svg></span>
</div>
<div class="hero-bar abs">
  <div class="l1">DELICIOUS, BEVERAGES AND GREAT-TASTING FOOD</div>
  <div class="l2">THE SECRET TO MAKING LIFE BETTER</div>
  <span class="dl script">Download our full menu</span>
</div>

<section class="menu-box abs">
  <div class="menu-head">Breakfast Menu</div>
  <div class="menu-item"><span class="thumb ph" role="img" aria-label="Photo of a breakfast plate" style="background:#c98a52"></span><span class="price">$15.00</span></div>
  <div class="menu-item"><span class="thumb ph" role="img" aria-label="Photo of a breakfast sandwich" style="background:#a86a3c"></span><span class="price">$9.00</span></div>
  <div class="menu-list">
    <div class="menu-row">Brunch Menu<i>+</i></div>
    <div class="menu-row">Lunch Menu<i>+</i></div>
    <div class="menu-row">Dinner Menu<i>+</i></div>
  </div>
</section>

<section class="featured abs">
  <div class="sec-head">FEATURED DISHES</div>
  <div class="dish ph" style="left:20px;background:linear-gradient(135deg,#f2d27a,#d9412a)" role="img" aria-label="Photo of penne pasta with tomatoes"></div>
  <div class="dish ph" style="left:276px;background:linear-gradient(135deg,#f0c06a,#c4432c)" role="img" aria-label="Photo of a pizza slice"></div>
  <div class="dish ph" style="left:534px;background:linear-gradient(135deg,#d6e07a,#6aa33a)" role="img" aria-label="Photo of green spinach pasta"></div>
  <div class="dish-price abs" style="left:95px;top:284px">$35.00</div>
  <div class="dish-price abs" style="left:351px;top:284px">$17.00</div>
  <div class="dish-price abs" style="left:609px;top:284px">$12.00</div>
  <div class="nav-dot abs" style="left:-12px;top:193px">‹</div>
  <div class="nav-dot abs" style="left:762px;top:193px">›</div>
</section>

<h2 class="blog-title abs">Latest from Our Blog</h2>
<div class="blog-rule abs"></div>
<div class="post-date date-box abs"><b>21</b><small>SEP 2014</small></div>
<div class="post-meta abs">By: admin &nbsp;|&nbsp; Comments: 0</div>
<h3 class="post-heading abs">Food for cardio concious people</h3>
<div class="post-img ph" style="background:linear-gradient(135deg,#7fb04a,#d2452e)" role="img" aria-label="Photo of a cheese salad with tomatoes"></div>
<div class="post-body abs">
  <h4>CHEESE SALAD</h4>
  <p>Fresh greens, aged cheddar and ripe tomatoes tossed in a light herb dressing. A hearty plate that keeps the heart happy and the table full all week.</p>
  <p>Our kitchen uses local produce picked each morning, olive oil instead of butter and plenty of crunchy seeds for a filling meal.</p>
  <p>Read the full recipe below.</p>
</div>
<div class="mini-posts abs">
  <div class="mini"><span class="d date-box">15<small>SEP</small></span><span class="t" style="background:#b07040" role="img" aria-label="Photo of a plated dish"></span><span class="x">Food for thought<span>by: Nora Pell</span></span></div>
  <div class="mini"><span class="d date-box">10<small>SEP</small></span><span class="t" style="background:#d49a4a" role="img" aria-label="Photo of spiced rice"></span><span class="x">Bombay Biryani<span>by: Dev Arlen</span></span></div>
  <div class="mini"><span class="d date-box">06<small>SEP</small></span><span class="t" style="background:#6b4a32" role="img" aria-label="Photo of a coffee cup"></span><span class="x">Special Coffee<span>by: Tova Reed</span></span></div>
</div>

<aside class="critic abs">
  <div class="critic-head"><h3>Marla Quincey</h3><p>Food Critic</p></div>
  <div class="avatar abs" role="img" aria-label="Portrait of the food critic"></div>
  <div class="quote abs">So far, a very good experience and food was really yummy! Warm service, fair prices and the best biscuits in town.</div>
  <div class="review-field abs"></div>
  <div class="review-btn abs">+ ADD YOUR REVIEW</div>
</aside>

<section class="deal abs">
  <div class="deal-red abs"></div>
  <div class="deal-plate ph" role="img" aria-label="Plate of spaghetti"></div>
  <div class="deal-script abs script">Deliciousness,<br>made for you.</div>
  <div class="deal-copy abs">half off delivery from 8-10Pm<br>monday - thursday</div>
  <div class="deal-badge abs script">Happy Hour!</div>
</section>

<section class="today abs">
  <div class="day">MONDAY</div>
  <div class="num">27</div>
  <div class="time">7:00 pm – 11:30 PM</div>
  <div class="evt">FOOD GALA</div>
</section>
<section class="cal abs">
  <div class="cal-head"><span>‹</span><span>September 2014</span><span>›</span></div>
  <div class="cal-grid">
    <b>S</b><b>M</b><b>T</b><b>W</b><b>T</b><b>F</b><b>S</b>
    <span></span><span>1</span><span>2</span><span>3</span><span>4</span><span>5</span><span>6</span>
    <span>7</span><span>8</span><span>9</span><span>10</span><span>11</span><span>12</span><span>13</span>
    <span>14</span><span>15</span><span>16</span><span>17</span><span>18</span><span>19</span><span>20</span>
    <span>21</span><span>22</span><span>23</span><span>24</span><span>25</span><span>26</span><span>27</span>
    <span>28</span><span class="on">29</span><span>30</span><span></span><span></span><span></span><span></span>
  </div>
</section>
<section class="events abs">
  <div class="events-head">Events &amp; Happenings</div>
  <div class="evt-row"><span class="pic ph" style="background:linear-gradient(135deg,#e6b04a,#b8401e)" role="img" aria-label="Photo of Thai noodles"></span>
    <div class="info"><b>24</b> sep<em>Thai Food Carnival</em><p>A night of street noodles, curries and sweet mango desserts.</p></div></div>
  <div class="evt-row"><span class="pic ph" style="background:linear-gradient(135deg,#f0d070,#c88a2a)" role="img" aria-label="Photo of baked pastries"></span>
    <div class="info"><b>16</b> sep<em>Baking Competition</em><p>Bring your best biscuits and pies to win a year of coffee.</p></div></div>
</section>
<section class="meet abs">
  <div class="meet-head">Meet us!<svg width="22" height="22" viewBox="0 0 24 24"><path d="M12 2a7 7 0 0 0-7 7c0 5 7 13 7 13s7-8 7-13a7 7 0 0 0-7-7zm0 9.5A2.5 2.5 0 1 1 12 6.5a2.5 2.5 0 0 1 0 5z" fill="#fff"/></svg></div>
  <div class="map ph" role="img" aria-label="Street map showing the diner location"></div>
  <svg class="abs" style="left:108px;top:140px" width="24" height="32" viewBox="0 0 24 32"><path d="M12 0a11 11 0 0 0-11 11c0 8 11 21 11 21s11-13 11-21A11 11 0 0 0 12 0z" fill="#b3121c"/><circle cx="12" cy="11" r="4" fill="#fff"/></svg>
  <div class="meet-foot abs">ALL WEEK</div>
</section>

<div class="chef-photo ph" role="img" aria-label="Photo of the head chef in whites"></div>
<div class="chef-social abs"><span></span><span></span><span></span><span></span></div>
<section class="chef-info abs">
  <div class="chef-head">Elliot Varga
    <div class="chef-arrows"><span><svg width="10" height="14"><path d="M8 1 2 7l6 6" stroke="#fff" stroke-width="2" fill="none"/></svg></span><span><svg width="10" height="14"><path d="M2 1l6 6-6 6" stroke="#fff" stroke-width="2" fill="none"/></svg></span></div>
  </div>
  <div class="chef-sub abs">Major expertise of our chef</div>
  <ul class="chef-list abs">
    <li>Slow-smoked meats and gravies</li><li>Homemade biscuits every morning</li>
    <li>Seasonal farm vegetables</li><li>Family recipes passed down</li>
  </ul>
  <div class="skills abs">
    <div class="skill"><svg width="76" height="76"><circle cx="38" cy="38" r="32" stroke="#e5e5e5" stroke-width="5" fill="none"/><circle cx="38" cy="38" r="32" stroke="#b3121c" stroke-width="5" fill="none" stroke-dasharray="181 201" transform="rotate(-90 38 38)"/><text x="38" y="43" text-anchor="middle" font-size="14" font-family="Open Sans,sans-serif">90%</text></svg><br>BAKING EXPERT</div>
    <div class="skill"><svg width="76" height="76"><circle cx="38" cy="38" r="32" stroke="#e5e5e5" stroke-width="5" fill="none"/><circle cx="38" cy="38" r="32" stroke="#b3121c" stroke-width="5" fill="none" stroke-dasharray="141 201" transform="rotate(-90 38 38)"/><text x="38" y="43" text-anchor="middle" font-size="14" font-family="Open Sans,sans-serif">70%</text></svg><br>CHINESE FOOD</div>
    <div class="skill"><svg width="76" height="76"><circle cx="38" cy="38" r="32" stroke="#e5e5e5" stroke-width="5" fill="none"/><circle cx="38" cy="38" r="32" stroke="#b3121c" stroke-width="5" fill="none" stroke-dasharray="161 201" transform="rotate(-90 38 38)"/><text x="38" y="43" text-anchor="middle" font-size="14" font-family="Open Sans,sans-serif">80%</text></svg><br>BAKING EXPERT</div>
    <div class="skill"><svg width="76" height="76"><circle cx="38" cy="38" r="32" stroke="#b3121c" stroke-width="5" fill="none"/><text x="38" y="43" text-anchor="middle" font-size="14" font-family="Open Sans,sans-serif">100%</text></svg><br>CHINESE FOOD</div>
  </div>
</section>
<section class="video abs">
  <div class="video-head"><b>Video of the Month</b><small>RECIPE OF CHICKEN FAJITA PIZZA</small></div>
  <div class="video-img ph" style="background:linear-gradient(135deg,#e9b85a,#b3421f)" role="img" aria-label="Video still of a chicken fajita pizza"></div>
  <div class="video-bar abs"><svg style="margin:8px 10px" width="14" height="14"><path d="M2 1l11 6-11 6z" fill="#fff"/></svg></div>
</section>

<footer class="footer abs"></footer>
<div class="f-col abs" style="left:81px;width:240px">
  <div class="f-title">Featured Dishes</div>
  <div class="f-item"><span class="th" style="background:#c07a3a" role="img" aria-label="Fried chicken"></span>Fried Chicken with almond sauce</div>
  <div class="f-item"><span class="th" style="background:#8a4a2a" role="img" aria-label="Beef steak"></span>Beef Steak with jalapeno Sauce</div>
  <div class="f-item"><span class="th" style="background:#9a5a32" role="img" aria-label="Beef steak"></span>Beef Steak with jalapeno Sauce</div>
</div>
<div class="f-col abs" style="left:345px;width:240px">
  <div class="f-title">Recent Blog Posts</div>
  <div class="f-item"><span class="dd date-box">Sep<small>2013</small></span><span class="th" style="width:60px;background:#7a9a4a" role="img" aria-label="Salad bowl"></span>Balanced diet facts unleashed</div>
  <div class="f-item"><span class="dd date-box">Sep<small>2013</small></span><span class="th" style="width:60px;background:#c8703a" role="img" aria-label="Street cooking"></span>Cooking experts on the streets</div>
  <div class="f-item"><span class="dd date-box">Sep<small>2013</small></span><span class="th" style="width:60px;background:#b8883a" role="img" aria-label="Stuffed chicken"></span>Tips for stuffed chicken</div>
</div>
<div class="f-col abs" style="left:614px;width:240px">
  <div class="f-title">Contact Us Now!</div>
  <div class="input">Name</div>
  <div class="input">Email</div>
  <div class="input textarea">Message</div>
  <div class="submit">SUBMIT</div>
</div>
<div class="clock ph" style="background:radial-gradient(circle,#f4f4f4 0 38%,#444 39% 100%)" role="img" aria-label="Illustration of a plate clock between a fork and spoon showing opening hours"></div>
<div class="reserve abs">For Table Reservation <b>0800 555 0142</b><br><span style="font-weight:400;color:#777">Weekdays 11am–9pm</span></div>

<div class="tweet abs"><span class="ic"></span>Tilden's Biscuit Barn @ Announced free dinner for couples getting married on this Christmas! &nbsp; Visit our site tildensbarn-example.com
  <div class="dots"><i class="on"></i><i></i><i></i><i></i></div>
</div>
<section class="collection abs"></section>
<div class="coll-title f-title abs">Chef's Collection</div>
<div class="coll-item abs" style="left:81px"><span class="th" style="background:#b8602a" role="img" aria-label="Fajita pizza"></span><div><b>Fajita Pizza with Extra Cheese</b><span>Peppers, chicken, onions, cheese</span></div></div>
<div class="coll-item abs" style="left:436px"><span class="th" style="background:#7a9a3a" role="img" aria-label="Fajita pizza"></span><div><b>Fajita Pizza with Extra Cheese</b><span>Peppers, chicken, onions, cheese</span></div></div>
<div class="coll-item abs" style="left:790px"><span class="th" style="background:#c8883a" role="img" aria-label="Fajita pizza"></span><div><b>Fajita Pizza with Extra Cheese</b><span>Peppers, chicken, onions, cheese</span></div></div>

<div class="base abs">© 2014 Tilden's Biscuit Barn</div>
<div class="to-top abs"><svg width="14" height="10"><path d="M1 9l6-6 6 6" stroke="#fff" stroke-width="2" fill="none"/></svg></div>
<div class="foot-social abs"><span></span><span></span><span></span><span></span><span></span><span></span></div>

</body>
</html>
```